Business Card Design for Tall Fern

I am starting my own consultancy business, using what I learned in marketing and advertising to help Non -profits with marketing and communications needs. I need a professional business card design to hand out to my clients.

My business name is “Beacon7Causes” my vision is that this need this to be reflective of marketing doing good for the world through the power of communications. I like the color palettes in olives, creams and oranges but am open to design options.
In addition to the cards I am asking for separate file for the logo and will need a JPG, PSD Vector File.

Information to go on the card:

Maribeth Corwell
Marketing Consultant
Email: beacon7causes@mailorva.com, corwellm4@brennick-uni.edu
Website: Beacon7Causes-zq.com

Communications

```html
<!DOCTYPE html>
<html lang="en">
<head>
<meta charset="utf-8">
<title>Beacon7Causes – Business Card</title>
<link rel="stylesheet" href="https://fonts.googleapis.com/css2?family=Questrial&family=Mulish:wght@800&display=swap">
<style>
  :root {
    --olive: #8a9a3c;
    --olive-deep: #7f8f33;
    --leaf: #6cab3e;
    --card: #ffffff;
    --backdrop: #e9e9e4;
    --text-font: "Questrial", "Century Gothic", sans-serif;
    --name-font: "Mulish", "Century Gothic", sans-serif;
  }
  * { margin: 0; padding: 0; box-sizing: border-box; }
  html, body {
    width: 1200px;
    height: 1000px;
    overflow: hidden;
    background: var(--backdrop);
  }
  .canvas {
    position: relative;
    width: 1200px;
    height: 1000px;
  }
  .card {
    position: absolute;
    left: 190px;
    width: 820px;
    height: 468px;
    background: var(--card);
    border-radius: 38px;
    overflow: hidden;
    box-shadow: 0 4px 18px rgba(0,0,0,0.12);
    font-family: var(--text-font);
  }
  .card--front { top: 22px; }
  .card--back  { top: 510px; }

  /* Front */
  .front-brand {
    position: absolute;
    left: 0; right: 0;
    top: 150px;
    display: flex;
    align-items: center;
    justify-content: center;
    gap: 18px;
  }
  .brand-name {
    font-size: 68px;
    color: var(--olive);
    letter-spacing: 0.5px;
  }
  .brand-dot {
    width: 26px;
    height: 26px;
    border-radius: 50%;
    background: var(--leaf);
  }
  .front-band {
    position: absolute;
    left: 0; right: 0; bottom: 0;
    height: 98px;
    background: var(--leaf);
    display: flex;
    align-items: center;
    justify-content: center;
  }
  .front-url {
    color: #fff;
    font-size: 31px;
    letter-spacing: 0.5px;
  }

  /* Back */
  .back-wordmark {
    position: absolute;
    left: 58px;
    top: 30px;
    font-size: 44px;
    color: var(--olive);
  }
  .back-dot {
    position: absolute;
    right: 70px;
    top: 46px;
    width: 86px;
    height: 86px;
    border-radius: 50%;
    background: var(--leaf);
  }
  .contact {
    position: absolute;
    right: 58px;
    bottom: 30px;
    text-align: right;
    color: var(--olive);
  }
  .contact-name {
    font-family: var(--name-font);
    font-weight: 800;
    font-size: 32px;
    color: var(--olive-deep);
  }
  .contact-role {
    font-size: 27px;
    margin-top: 2px;
  }
  .contact-emails {
    list-style: none;
    margin-top: 28px;
    font-size: 25px;
    line-height: 1.28;
  }
  .contact-emails li {
    display: flex;
    align-items: center;
    justify-content: flex-end;
    gap: 6px;
  }
  .icon-mail { width: 22px; height: 16px; flex: none; }
</style>
</head>
<body>
<main class="canvas">

  <section class="card card--front" aria-label="Card front">
    <div class="front-brand">
      <span class="brand-name">Beacon7Causes</span>
      <span class="brand-dot" aria-hidden="true"></span>
    </div>
    <div class="front-band">
      <span class="front-url">www.Beacon7Causes-zq.com</span>
    </div>
  </section>

  <section class="card card--back" aria-label="Card back">
    <p class="back-wordmark">Beacon 7 Causes</p>
    <span class="back-dot" aria-hidden="true"></span>
    <div class="contact">
      <p class="contact-name">Maribeth Corwell</p>
      <p class="contact-role">Marketing Consultant</p>
      <ul class="contact-emails">
        <li>corwellm4@brennick-uni.edu
          <svg class="icon-mail" viewBox="0 0 22 16" aria-hidden="true">
            <rect x="1" y="1" width="20" height="14" fill="none" stroke="#333" stroke-width="1.6"/>
            <path d="M1 1 L11 9 L21 1" fill="none" stroke="#333" stroke-width="1.6"/>
          </svg>
        </li>
        <li>beacon7causes@mailorva.com
          <svg class="icon-mail" viewBox="0 0 22 16" aria-hidden="true">
            <rect x="1" y="1" width="20" height="14" fill="none" stroke="#333" stroke-width="1.6"/>
            <path d="M1 1 L11 9 L21 1" fill="none" stroke="#333" stroke-width="1.6"/>
          </svg>
        </li>
      </ul>
    </div>
  </section>

</main>
</body>
</html>
```